Legal Service Estimated Retainer and Average Case Value

We need an 11x14 flyer that contains the standard retainers and average cost be case, both provided in documents, for each case type we handle. We need the information displayed, preferably in a way that makes the information readable but less troubling to a client shocked at price of litigation. We need one sheet with the retainers and average case value merged into one table.

Target Market(s)

Potential Clients

Font styles to use
Serif
Sans Serif

```html
<!DOCTYPE html>
<html lang="en">
<head>
<meta charset="utf-8">
<title>Legal Service Estimated Retainer and Average Case Value</title>
<link href="https://fonts.googleapis.com/css2?family=Cinzel:wght@600;700&family=Montserrat:wght@400;500&display=swap" rel="stylesheet">
<style>
  :root {
    --page-bg: #e9e6e1;
    --paper: #ffffff;
    --navy: #17263a;
    --teal: #1f5f6e;
    --ink: #1b1b1b;
    --rule: #2a2a2a;
    --row-shade: #d8d9db;
    --photo-warm: #c9a58b;
    --photo-deep: #6e4e3c;
  }
  * { box-sizing: border-box; margin: 0; padding: 0; }
  html, body { width: 1200px; height: 1200px; overflow: hidden; background: var(--page-bg); }
  .stage { position: relative; width: 1200px; height: 1200px; }
  .flyer {
    position: absolute; left: 144px; top: 20px;
    width: 1057px; height: 1344px;
    transform: scale(0.863); transform-origin: 0 0;
    background: var(--paper);
    box-shadow: 0 6px 24px rgba(0,0,0,.18);
    overflow: hidden;
  }
  .portrait-strip {
    position: absolute; left: 0; top: 125px; width: 1057px; height: 288px;
    background: linear-gradient(90deg, var(--photo-warm), #d9b59a 30%, var(--photo-deep) 55%, #d4b099 75%, #4a3426);
  }
  .header-art { position: absolute; left: 0; top: 0; width: 1057px; height: 150px; }
  .firm-name {
    position: absolute; left: 52px; top: 48px;
    display: flex; align-items: center; gap: 14px;
    font-family: "Cinzel", serif; font-weight: 600; color: var(--navy);
  }
  .firm-name .mark { width: 18px; height: 18px; background: var(--navy); }
  .firm-name .label { font-size: 26px; line-height: 1; }
  .banner-title {
    position: absolute; left: 504px; top: 28px; color: #fff;
    font-family: "Cinzel", serif; font-weight: 700;
  }
  .banner-title .line1 { font-size: 36px; letter-spacing: .5px; }
  .banner-title .line2 { font-size: 24px; margin-top: 6px; letter-spacing: .3px; }
  .fee-panel {
    position: absolute; left: 60px; top: 418px; width: 937px; height: 896px;
    background: var(--paper);
    box-shadow: 0 0 6px rgba(0,0,0,.35);
  }
  .fee-intro {
    margin: 0 3px; height: 115px; padding: 16px 34px 0;
    background: linear-gradient(90deg, var(--navy), #1c3447 80%, var(--teal));
    color: #fff;
  }
  .fee-intro h2 { font-family: "Cinzel", serif; font-weight: 700; font-size: 22px; letter-spacing: .2px; }
  .fee-intro p { font-family: "Montserrat", sans-serif; font-size: 14.6px; line-height: 19.5px; margin-top: 4px; }
  .fee-table { width: 931px; margin: 4px 3px 0; border-collapse: collapse; font-family: "Montserrat", sans-serif; font-size: 15.5px; color: var(--ink); }
  .fee-table td { height: 29.4px; border-bottom: 1.5px solid var(--rule); vertical-align: middle; }
  .fee-table .case-type { width: 573px; padding-left: 40px; border-right: 2px solid var(--rule);
    background: linear-gradient(90deg, #fff 0%, #fff 35%, var(--row-shade) 100%); }
  .fee-table .fee { padding-left: 54px; }
  .fee-table .group-break td { height: 8px; border-bottom: 1.5px solid var(--rule); }
  .fee-table tr:last-child td { border-bottom: none; }
</style>
</head>
<body>
<div class="stage">
  <div class="flyer">
    <div class="portrait-strip" role="img" aria-label="Row of smiling client headshot photographs"></div>
    <svg class="header-art" viewBox="0 0 1057 150" aria-hidden="true">
      <defs>
        <linearGradient id="bannerFill" x1="0" x2="1">
          <stop offset="0" stop-color="#1f5f6e"/>
          <stop offset="1" stop-color="#17263a"/>
        </linearGradient>
      </defs>
      <polygon points="490,0 1057,0 1057,125 428,125" fill="url(#bannerFill)"/>
      <polygon points="0,0 490,0 428,147 0,147" fill="#ffffff"/>
    </svg>
    <div class="firm-name">
      <span class="mark"></span>
      <span class="label">Daniel M Whitford Law</span>
    </div>
    <div class="banner-title">
      <div class="line1">LEGAL SERVICE ESTIMATED</div>
      <div class="line2">RETAINER AND AVERAGE CASE VALUE</div>
    </div>

    <section class="fee-panel">
      <div class="fee-intro">
        <h2>THE RETAINER AND THE AVERAGE FEE PER CASE TYPE</h2>
        <p>In order for our clients to set expectations for legal fees, we provide the national average range of fees per case type. These are only to provide you with an understanding of what other cases have cost clients in similar cases. Please note these are not estimates nor guarantees of your own legal costs.</p>
      </div>
      <table class="fee-table">
        <tr><td class="case-type">Divorce (3301c)</td><td class="fee">$1,500 - $3,000</td></tr>
        <tr><td class="case-type">Divorce (3301d)</td><td class="fee">$2,000 - $3,000</td></tr>
        <tr><td class="case-type">Custody Initial Order</td><td class="fee">$4,000 - $7,000</td></tr>
        <tr><td class="case-type">Custody Contempt/Modification</td><td class="fee">$5,000 - $8,000</td></tr>
        <tr><td class="case-type">Custody &amp; Support</td><td class="fee">$5,000 - $8,000</td></tr>
        <tr><td class="case-type">Support</td><td class="fee">$2,000 - $4,000</td></tr>
        <tr><td class="case-type">Protection from Abuse</td><td class="fee">$1,500 - $3,000</td></tr>
        <tr><td class="case-type">Divorce &amp; Custody</td><td class="fee">$5,000 - $8,000</td></tr>
        <tr><td class="case-type">Divorce &amp; Equitable Distribution</td><td class="fee">$6,000 - $10,000</td></tr>
        <tr><td class="case-type">Divorce, Custody &amp; Support</td><td class="fee">$8,000 - $12,000</td></tr>
        <tr><td class="case-type">Divorce, Equitable Distribution &amp; Custody</td><td class="fee">$10,000 - $15,000</td></tr>
        <tr><td class="case-type">Divorce, Equitable Distribution &amp; Support</td><td class="fee">$8,000 - $12,000</td></tr>
        <tr><td class="case-type">Divorce, Equitable Distribution, Custody &amp; Support</td><td class="fee">$12,000 - $15,000</td></tr>
        <tr class="group-break"><td class="case-type"></td><td class="fee"></td></tr>
        <tr><td class="case-type">Divorce (3301 C)</td><td class="fee">Retainer: $2,000</td></tr>
        <tr><td class="case-type">Divorce (3301 D)</td><td class="fee">Retainer: $2,500</td></tr>
        <tr><td class="case-type">Divorce and Custody</td><td class="fee">Retainer: $3,500</td></tr>
        <tr><td class="case-type">Divorce and Equitable Distribution</td><td class="fee">Retainer: $3,500</td></tr>
        <tr><td class="case-type">Divorce and Support</td><td class="fee">Retainer: $3,000</td></tr>
        <tr><td class="case-type">Divorce, Custody and Support</td><td class="fee">Retainer: $3,500</td></tr>
        <tr><td class="case-type">Divorce, Equitable Distribution and Support</td><td class="fee">Retainer: $3,500</td></tr>
        <tr><td class="case-type">Divorce, Equitable Distribution and Custody</td><td class="fee">Retainer: $5,000</td></tr>
        <tr><td class="case-type">Divorce, Equitable Distribution, Custody and Support</td><td class="fee">Retainer: $3,500</td></tr>
        <tr><td class="case-type">Custody Initial Order</td><td class="fee">Retainer: $3,000</td></tr>
        <tr><td class="case-type">Custody Modification</td><td class="fee">Retainer: $3,500</td></tr>
        <tr><td class="case-type">Custody and Support</td><td class="fee">Retainer: $3,000</td></tr>
        <tr><td class="case-type">Protection From Abuse (PFA)</td><td class="fee">$2,000 Paid In Full</td></tr>
      </table>
    </section>
  </div>
</div>
</body>
</html>
```